Banner Ad Design Project: rolverantco.com

Google all ad dimensions banner pack for http://www.rolverantco.com.

Ad dimensions Max. file sizes (KB) Ad types
468 × 60 50 Banner
728 × 90 50 Leaderboard
250 × 250 50 Square
200 × 200 50 Small square
336 × 280 50 Large rectangle
300 × 250 50 Inline rectangle
120 × 600 50 Skyscraper
160 × 600 50 Wide skyscraper
300 × 600 200 Half-page ad
970 × 90 200 Large leaderboard
240 × 400 50 Vertical rectangle
980 × 120 200 Panorama
930 × 180 200 Top banner
250 × 360 50 Triple widescreen
580 × 400 200 Netboard

*Please visit the website and come up with unique ideas.

Target Market(s)

Consumers looking to transport a car, motor vehicle, motorcycle or anything that has wheels and a motor in the united states long distance.

Industry/Entity Type

Google

Requirements
Must have
• a call to action for example (RANDOM ONE):
-
TALK TO A REAL CAR SHIPPING PRO NOW: 1-888-614-2753
HAVE CAR TRANSPORT QUESTIONS? CALL NOW: 1-888-614-2753
CALL NOW & TALK TO A REAL AUTO SHIPPING EXPERT: 1-888-614-2753
Call Now Free Quote:1-888-614-2753

Nice to have
• Best Value For Dollar Auto Transport
Bonded, Insured & Licensed
Price Match Guarantee: will match any price by a 4 or 5 star rated Company.
Best of all, you pay nothing until your car is picked up!
Nationwide Door-To-Door Vehicle Shipping
Should not have
• Logo integrated in to the design.
bold call to action; ex; call now free quote:
Heading style phone number, 888-614-2753, stands out and screams call now.
example:
CALL ROLVERANT TODAY TO TRANSPORT YOUR VEHICLE
1-888-614-2753

```html
<!DOCTYPE html>
<html lang="en">
<head>
<meta charset="utf-8">
<title>rolverantco.com banner pack</title>
<link rel="stylesheet" href="https://fonts.googleapis.com/css2?family=Cabin:wght@400;500&family=Montserrat:wght@800&family=PT+Sans&display=swap">
<style>
  :root {
    --sheet: #f4f4f5;
    --sheet-edge: #e6e6e8;
    --label: #111111;
    --ad-yellow: #fbe04a;
    --ad-orange: #f6ae2e;
    --ad-deep: #f49a24;
    --purple: #8e2b8e;
    --purple-bright: #a9309b;
    --black: #0d0d0d;
    --truck: #b8bcc2;
    --truck-dark: #3c3f44;
    --bike: #c8201f;
    --bike-dark: #3a1414;
    --car: #4a4d57;
    --car-dark: #23252c;
  }
  * { margin: 0; padding: 0; box-sizing: border-box; }
  html, body { width: 1200px; height: 850px; overflow: hidden; }
  body {
    position: relative;
    background: radial-gradient(ellipse at 50% 40%, #fbfbfb 0%, var(--sheet) 60%, var(--sheet-edge) 100%);
    font-family: "PT Sans", Arial, sans-serif;
  }
  .size-label {
    position: absolute;
    font-size: 21px;
    color: var(--label);
    white-space: pre;
  }
  .ad {
    position: absolute;
    overflow: hidden;
    background: radial-gradient(ellipse at 55% 55%, var(--ad-yellow) 0%, var(--ad-orange) 65%, var(--ad-deep) 100%);
  }
  .ad-visual { position: absolute; }
  .headline, .phone {
    position: absolute;
    white-space: nowrap;
    font-family: "Cabin", "Gill Sans", sans-serif;
    color: var(--purple);
  }
  .phone {
    background: linear-gradient(90deg, var(--purple-bright), var(--purple));
    -webkit-background-clip: text;
    background-clip: text;
    color: transparent;
    font-weight: 400;
  }

  /* 468 x 60 banner */
  .ad-banner { left: 278px; top: 102px; width: 644px; height: 82px; }
  .ad-banner .ad-visual {
    left: 2px; top: 0; width: 138px; height: 82px;
    border-radius: 4px 10px 6px 4px;
    background: linear-gradient(135deg, var(--truck-dark) 0%, var(--truck) 45%, #e3e5e8 70%, var(--truck) 100%);
  }
  .ad-banner .headline { left: 159px; top: 5px; font-size: 20.5px; letter-spacing: 1.6px; }
  .ad-banner .phone { left: 150px; top: 20px; font-size: 60px; letter-spacing: 2.6px; line-height: 1; }

  /* 728 x 90 leaderboard */
  .ad-leaderboard { left: 98px; top: 255px; width: 1004px; height: 124px; }
  .ad-leaderboard .ad-visual {
    left: 42px; top: 2px; width: 190px; height: 122px;
    border-radius: 40% 45% 40% 40%;
    background: linear-gradient(160deg, var(--bike) 0%, #e23a2c 40%, var(--bike-dark) 100%);
  }
  .ad-leaderboard .headline { left: 240px; top: 6px; font-size: 31px; letter-spacing: 2.6px; }
  .ad-leaderboard .phone { left: 236px; top: 28px; font-size: 96px; letter-spacing: 4px; line-height: 1; }

  /* 250 x 250 square */
  .ad-square { left: 429px; top: 441px; width: 343px; height: 344px; }
  .ad-square .headline {
    left: 0; width: 100%; top: 40px;
    text-align: center;
    font-family: "Montserrat", "Futura", sans-serif;
    font-weight: 800;
    font-size: 19.5px;
    line-height: 26.5px;
    letter-spacing: 1.6px;
    color: var(--black);
  }
  .ad-square .phone { left: 0; width: 100%; text-align: center; top: 148px; font-size: 36px; letter-spacing: 1.6px; line-height: 1; }
  .ad-square .ad-visual {
    left: 56px; top: 206px; width: 242px; height: 136px;
    border-radius: 45% 40% 18% 18%;
    background: linear-gradient(170deg, #7b7f8a 0%, var(--car) 45%, var(--car-dark) 100%);
  }
</style>
</head>
<body>
  <p class="size-label" style="left:486px; top:71px;">468 × 60   50    Banner</p>
  <section class="ad ad-banner" aria-label="468 by 60 banner">
    <div class="ad-visual" role="img" aria-label="Silver delivery truck cab"></div>
    <p class="headline">TALK TO A REAL CAR SHIPPING PRO NOW</p>
    <p class="phone">1-888-614-2753</p>
  </section>

  <p class="size-label" style="left:457px; top:221px;">728 × 90   50    Leaderboard</p>
  <section class="ad ad-leaderboard" aria-label="728 by 90 leaderboard">
    <div class="ad-visual" role="img" aria-label="Red sport motorcycle"></div>
    <p class="headline">HAVE CAR TRANSPORT QUESTIONS? CALL NOW</p>
    <p class="phone">1-888-614-2753</p>
  </section>

  <p class="size-label" style="left:463px; top:412px;">250 × 250         50    Square</p>
  <section class="ad ad-square" aria-label="250 by 250 square">
    <p class="headline">CALL NOW &amp;<br>TALK TO<br>A REAL AUTO<br>SHIPPING EXPERT</p>
    <p class="phone">1-888-614-2753</p>
    <div class="ad-visual" role="img" aria-label="Dark grey luxury sedan"></div>
  </section>
</body>
</html>
```